I need to design a business card
on the front side the words "VELTRIS CAPITAL" with the top half surrounded by a stylised cloud. Minimalist, navy blue font on white background, with the Veltris capital in embossing.

On the back contact details (avoid centered). I would rather have the details taking the 2/3rd on the right and having the logo on the left, but anyway not plain centered

Marcello Lo Ruffo
CEO e Fondatore

m.loruffo@veltris-capital.example
+39.328.514.6082

Piazza Ventrano 7
20135 Milano

```html
<!DOCTYPE html>
<html lang="it">
<head>
<meta charset="utf-8">
<title>Veltris Capital – Biglietto da visita</title>
<link rel="stylesheet" href="https://fonts.googleapis.com/css2?family=Cinzel:wght@500;600&family=Montserrat:wght@400&display=swap">
<style>
  :root {
    --backdrop: #dcdcdc;
    --card: #f5f5f5;
    --navy: #1b2744;
    --ink: #2b2b2b;
  }
  * { box-sizing: border-box; margin: 0; padding: 0; }
  html, body {
    width: 1200px;
    height: 1124px;
    overflow: hidden;
    background: var(--backdrop);
  }
  .card {
    position: absolute;
    left: 252px;
    width: 696px;
    height: 398px;
    background: var(--card);
    border-radius: 28px;
    overflow: hidden;
  }
  .card--contact { top: 134px; }
  .card--brand { top: 592px; }

  .wordmark {
    position: absolute;
    font-family: "Cinzel", serif;
    font-weight: 600;
    color: var(--navy);
    text-align: center;
    line-height: 1;
  }
  .wordmark__name, .wordmark__sub { display: block; }

  .card--contact .wordmark { left: 38px; top: 88px; }
  .card--contact .wordmark__name {
    font-size: 34px;
    letter-spacing: 0.16em;
    padding-left: 0.16em;
  }
  .card--contact .wordmark__sub {
    margin-top: 7px;
    font-size: 14px;
    letter-spacing: 0.26em;
    padding-left: 0.26em;
  }

  .card--brand .wordmark { left: 0; right: 0; top: 196px; }
  .card--brand .wordmark__name {
    font-size: 58px;
    letter-spacing: 0.3em;
    padding-left: 0.3em;
  }
  .card--brand .wordmark__sub {
    margin-top: 14px;
    font-size: 25px;
    letter-spacing: 0.3em;
    padding-left: 0.3em;
  }

  .accent-bar {
    position: absolute;
    left: 0;
    top: 205px;
    width: 16px;
    height: 37px;
    background: var(--navy);
  }
  .person { position: absolute; left: 43px; top: 203px; }
  .person__name {
    font-family: "Cinzel", serif;
    font-weight: 600;
    font-size: 22px;
    color: var(--navy);
    line-height: 1;
    letter-spacing: 0.01em;
  }
  .person__role {
    margin-top: 3px;
    font-family: "Montserrat", sans-serif;
    font-size: 15.5px;
    color: var(--ink);
    line-height: 1.2;
  }

  .contacts, .address {
    position: absolute;
    top: 310px;
    list-style: none;
    font-family: "Montserrat", sans-serif;
    font-size: 16px;
    color: var(--ink);
    line-height: 25px;
  }
  .contacts { left: 41px; }
  .contacts li { display: flex; align-items: center; gap: 5px; }
  .contacts svg { width: 11px; height: 11px; fill: var(--navy); flex: none; }
  .address { right: 41px; text-align: right; }
</style>
</head>
<body>

<section class="card card--contact">
  <div class="wordmark">
    <span class="wordmark__name">VELTRIS</span>
    <span class="wordmark__sub">CAPITAL</span>
  </div>

  <span class="accent-bar"></span>
  <div class="person">
    <p class="person__name">MARCELLO LO RUFFO</p>
    <p class="person__role">CEO e Fondatore</p>
  </div>

  <ul class="contacts">
    <li>
      <svg viewBox="0 0 24 24" aria-hidden="true"><path d="M6.6 10.8a15.1 15.1 0 0 0 6.6 6.6l2.2-2.2a1 1 0 0 1 1-.25 11.4 11.4 0 0 0 3.6.57 1 1 0 0 1 1 1V20a1 1 0 0 1-1 1A17 17 0 0 1 3 4a1 1 0 0 1 1-1h3.5a1 1 0 0 1 1 1c0 1.25.2 2.45.57 3.57a1 1 0 0 1-.25 1z"/></svg>
      +39.328.514.6082
    </li>
    <li>
      <svg viewBox="0 0 24 24" aria-hidden="true"><path d="M12 2 2 9v13h20V9zm0 2.4 7.6 5.3L12 14.6 4.4 9.7zM4 11.6l8 5.2 8-5.2V20H4z"/></svg>
      m.loruffo@veltris-capital.example
    </li>
  </ul>

  <address class="address" style="font-style: normal;">
    Piazza Ventrano 7<br>
    20135 Milano
  </address>
</section>

<section class="card card--brand">
  <div class="wordmark">
    <span class="wordmark__name">VELTRIS</span>
    <span class="wordmark__sub">CAPITAL</span>
  </div>
</section>

</body>
</html>
```